Allied Health Clinic needs catchy poster ad for lightbox

We need a catchy and effective poster designed for our retail lightbox which is in a busy corridor. We are a multi disciplinary sports injury clinic offering a range of allied health services. Established in 1999. We need people to understand our business identity and services clearly. I have come up with a very rough idea as far as what I think the copy should contain. The picture is an example of what image I am trying to convey to the potential client. I am not a designer clearly. We specialise in treating difficult problems.
Size of the poster is 451mm x 741mm at 300dpi. We will then blow the image up to double this size which will be good enough resolution for the printing.

Target Market(s)

White collar professionals - male and female, active 20-50 range

Industry/Entity Type

Healthcare

Font styles to use
Sans Serif

Requirements
Nice to have
• Easy to read, polished, nice tie in to my logo colours

```html
<!DOCTYPE html>
<html lang="en">
<head>
<meta charset="utf-8">
<title>Corefield Physiotherapy – Lightbox Poster</title>
<link rel="stylesheet" href="https://fonts.googleapis.com/css2?family=Open+Sans:wght@600;700&family=Roboto+Condensed:wght@700&family=Oswald:wght@500&display=swap">
<style>
  :root {
    --stage: #222222;
    --paper: #f2f2f2;
    --lime: #a8e61d;
    --lime-deep: #86c91a;
    --leaf: #8fd12a;
    --ink: #3a3a3a;
    --brand-red: #9b1c22;
    --white: #ffffff;
    --photo-grey-a: #d9d9d9;
    --photo-grey-b: #9a9a9a;
  }
  * { box-sizing: border-box; margin: 0; padding: 0; }
  html, body { width: 1000px; height: 1200px; overflow: hidden; background: var(--stage); }
  .poster {
    position: absolute; left: 148px; top: 30px;
    width: 700px; height: 1148px; overflow: hidden;
    background: var(--paper);
    font-family: "Open Sans", sans-serif; color: var(--ink);
  }
  .backdrop-photo {
    position: absolute; left: 120px; top: 110px; width: 580px; height: 650px;
    background: radial-gradient(ellipse at 70% 30%, var(--photo-grey-a), rgba(242,242,242,0) 70%);
    opacity: .8;
  }
  .shapes { position: absolute; inset: 0; }
  .brand {
    position: absolute; left: 60px; top: 210px; width: 600px;
    display: flex; align-items: center; gap: 14px;
    color: var(--ink); font-weight: 600;
  }
  .brand-dot { width: 30px; height: 30px; border-radius: 50%; background: var(--leaf); flex: none; }
  .brand-name { font-size: 27px; line-height: 1.25; letter-spacing: 1.5px; text-transform: uppercase; }
  .brand-name span { display: block; font-size: 17px; letter-spacing: 6px; }
  .headline {
    position: absolute; left: 85px; top: 332px;
    font-family: "Roboto Condensed", sans-serif; font-weight: 700;
    font-size: 40px; line-height: 1.08; color: var(--brand-red); text-transform: uppercase;
  }
  .injury-photo {
    position: absolute; width: 226px; height: 226px; border-radius: 50%;
    border: 7px solid var(--leaf);
    background: radial-gradient(circle at 45% 40%, var(--photo-grey-a), var(--photo-grey-b));
  }
  .injury-photo.runner { left: 40px; top: 458px; background: radial-gradient(circle at 40% 40%, #6e6e6e, #2a2a2a); }
  .injury-photo.skier { left: 229px; top: 458px; }
  .injury-photo.boot { left: 444px; top: 458px; background: radial-gradient(circle at 60% 40%, #c8c8c8, #555555); }
  .tagline {
    position: absolute; left: 68px; top: 722px;
    font-family: "Oswald", sans-serif; font-weight: 500;
    font-size: 24px; color: var(--brand-red); text-transform: uppercase; letter-spacing: .2px;
  }
  .services { position: absolute; left: 100px; top: 804px; }
  .services-title {
    font-family: "Open Sans", sans-serif; font-weight: 700;
    font-size: 26px; color: var(--brand-red); text-transform: uppercase;
    margin-bottom: 6px;
  }
  .service-list { list-style: none; padding-left: 5px; }
  .service-list li {
    font-weight: 600; font-size: 20px; line-height: 29px; text-transform: uppercase;
    display: flex; align-items: center; gap: 10px;
  }
  .service-list li::before {
    content: ""; width: 18px; height: 18px; border-radius: 50%; background: var(--leaf);
  }
  .contact-bar {
    position: absolute; left: 0; top: 1025px; width: 700px; height: 108px;
    background: var(--white);
  }
  .directions {
    position: absolute; top: 12px; width: 100%; text-align: center;
    font-weight: 700; font-size: 31px; color: var(--ink);
  }
  .contact-item {
    position: absolute; top: 64px; display: flex; align-items: center; gap: 10px;
    font-weight: 700; font-size: 23px; color: var(--ink);
  }
  .contact-item.phone { left: 24px; }
  .contact-item.web { left: 264px; }
  .contact-item svg { width: 32px; height: 32px; fill: var(--ink); }
</style>
</head>
<body>
<main class="poster">
  <div class="backdrop-photo" role="img" aria-label="Faded black and white photo of American football players in action"></div>

  <svg class="shapes" viewBox="0 0 700 1148" aria-hidden="true">
    <path d="M0 0 H700 V40 Q430 160 0 190 Z" fill="var(--lime)"/>
    <path d="M0 0 H330 Q160 60 0 70 Z" fill="var(--lime-deep)" opacity=".35"/>
    <path d="M420 330 Q700 420 700 780 V1025 H0 V1022 Q520 975 640 720 Q700 480 420 330 Z" fill="var(--lime)"/>
    <path d="M420 330 Q640 420 660 640 Q690 480 420 330 Z" fill="var(--lime-deep)" opacity=".4"/>
    <rect x="0" y="1133" width="700" height="15" fill="var(--lime)"/>
  </svg>

  <div class="brand">
    <div class="brand-dot"></div>
    <div class="brand-name">Corefield Physiotherapy<span>&amp; Sports Injury Clinic</span></div>
  </div>

  <h1 class="headline">Injury experts<br>trusted by athlets</h1>

  <div class="injury-photo runner" role="img" aria-label="Soccer player running, with a red marker on the elbow injury"></div>
  <div class="injury-photo skier" role="img" aria-label="Skier on a slope, with a red marker on the knee injury"></div>
  <div class="injury-photo boot" role="img" aria-label="Football boot on turf, with a red marker on the ankle injury"></div>

  <p class="tagline">Successfuly treating difficult injuries since 1999</p>

  <section class="services">
    <h2 class="services-title">A complete range of services</h2>
    <ul class="service-list">
      <li>Sports physiotherapy</li>
      <li>Chiropractic</li>
      <li>Massage</li>
      <li>Podiatry</li>
      <li>Exercise physiology</li>
    </ul>
  </section>

  <footer class="contact-bar">
    <p class="directions">TAKE LIFTS TO LEVEL 8</p>
    <div class="contact-item phone">
      <svg viewBox="0 0 24 24" aria-hidden="true"><path d="M6.6 10.8a15.1 15.1 0 0 0 6.6 6.6l2.2-2.2a1 1 0 0 1 1-.25 11.4 11.4 0 0 0 3.6.57 1 1 0 0 1 1 1V20a1 1 0 0 1-1 1A17 17 0 0 1 3 4a1 1 0 0 1 1-1h3.5a1 1 0 0 1 1 1c0 1.25.2 2.45.57 3.57a1 1 0 0 1-.25 1z"/></svg>
      <span>8700 1234</span>
    </div>
    <div class="contact-item web">
      <svg viewBox="0 0 24 24" aria-hidden="true"><circle cx="12" cy="12" r="10"/><path d="M12 2a10 10 0 0 0 0 20M2 12h20M12 2c3 3 3 17 0 20" fill="none" stroke="#fff" stroke-width="1.5"/></svg>
      <span>corefieldphysio.example.com.au</span>
    </div>
  </footer>
</main>
</body>
</html>
```